Word Templates for Green Energy Consulting Company

Please see attached brief. This is what we'd like. Please note that we have also launched a PowerPoint template project and we want the two designs to be consistent. We encourage designers to submit to both contests. PowerPoint project is here: https://www.pixelbidhub.net/manage-project/brief/7319268

Font styles to use
Serif
Sans Serif

```html
<!DOCTYPE html>
<html lang="en">
<head>
<meta charset="utf-8">
<title>Verdant Ridge Group – Word Template Set</title>
<link rel="stylesheet" href="https://fonts.googleapis.com/css2?family=Montserrat:wght@500;700&family=Open+Sans:wght@400;600;700&display=swap">
<style>
  :root {
    --bg: #e4e4e4;
    --paper: #ffffff;
    --navy: #1e2b48;
    --green: #1d8a3c;
    --lime: #7cc142;
    --brand-blue: #1b4f9c;
    --ink: #333a44;
    --muted: #8a8f96;
    --rule: #d3d6da;
  }
  * { box-sizing: border-box; margin: 0; padding: 0; }
  html, body { width: 1200px; height: 900px; overflow: hidden; background: var(--bg); }
  body { font-family: "Open Sans", Arial, sans-serif; color: var(--ink); }

  .sheet-grid {
    position: absolute; left: 125px; top: 25px;
    display: grid; grid-template-columns: repeat(3, 290px);
    grid-template-rows: repeat(2, 410px); gap: 30px 40px;
  }
  .page {
    position: relative; background: var(--paper); overflow: hidden;
    box-shadow: 0 4px 14px rgba(0,0,0,.12);
  }

  /* brand wordmark */
  .brand { font-family: "Montserrat", Arial, sans-serif; font-weight: 700; color: var(--brand-blue); line-height: 1.1; }
  .brand-row { display: flex; align-items: center; gap: 6px; }
  .brand-dot { width: 9px; height: 9px; background: var(--green); }
  .tagline { font-size: 7px; color: var(--green); margin-top: 2px; }

  /* footer */
  .page-foot { position: absolute; left: 16px; right: 16px; bottom: 10px; }
  .foot-rule { display: flex; height: 2px; }
  .foot-rule .navy { flex: 1; background: var(--navy); }
  .foot-rule .lime { flex: .35; background: var(--lime); }
  .foot-rule .green { flex: 1; background: var(--green); }
  .foot-text { display: flex; justify-content: space-between; font-size: 6px; margin-top: 3px; }
  .foot-text .site { color: var(--navy); }
  .foot-text .mail { color: var(--lime); }

  /* cover */
  .cover .brand-block { position: absolute; left: 40px; top: 105px; }
  .cover .brand { font-size: 15px; }
  .cover .doc-title { position: absolute; left: 40px; top: 158px; font-size: 21px; color: var(--green); font-weight: 400; }
  .cover .title-rule { position: absolute; left: 40px; right: 0; top: 192px; height: 2px; background: var(--green); }
  .cover .doc-sub { position: absolute; left: 40px; top: 202px; font-size: 7px; letter-spacing: .5px; color: var(--ink); }
  .cover .doc-company { position: absolute; left: 40px; top: 214px; font-size: 6px; color: var(--muted); }
  .cover .edge-bar { position: absolute; left: 0; top: 225px; width: 12px; height: 60px; background: var(--navy); border-right: 4px solid var(--lime); }

  /* letterhead */
  .letter .top-band { position: absolute; top: 0; left: 0; width: 290px; height: 30px; }
  .letter .brand-block { position: absolute; left: 18px; top: 30px; }
  .letter .brand { font-size: 12px; }
  .letter .outline { position: absolute; left: 24px; right: 20px; top: 78px; font-size: 6.3px; line-height: 1.45; color: #222; }
  .outline ol, .outline ul { padding-left: 11px; }
  .outline .lvl-b { list-style: lower-alpha; }
  .outline .lvl-i { list-style: lower-roman; }
  .outline .bold { font-weight: 700; }
  .letter .corner { position: absolute; right: 0; bottom: 0; width: 30px; height: 30px; }

  /* project cover */
  .project .bar-top { position: absolute; left: 0; top: 0; width: 14px; height: 122px; background: var(--lime); border-right: 2px solid var(--navy); }
  .project .bar-bottom { position: absolute; right: 0; bottom: 18px; width: 14px; height: 130px; background: var(--lime); border-left: 2px solid var(--navy); }
  .project .brand-block { position: absolute; left: 0; right: 0; top: 160px; text-align: center; }
  .project .brand { font-size: 17px; }
  .project .tag-line { display: flex; align-items: center; justify-content: center; gap: 5px; font-size: 7px; color: var(--green); margin-top: 3px; }
  .project .tag-line::before, .project .tag-line::after { content: ""; width: 20px; height: 1px; background: var(--green); }
  .project .pull-quote { position: absolute; right: 24px; bottom: 50px; width: 100px; font-size: 5.6px; line-height: 1.4; color: #222; }

  /* interior pages */
  .inner .head { position: absolute; left: 12px; right: 12px; top: 0; border-top: 3px solid var(--rule); padding-top: 8px; }
  .inner .brand { font-size: 8px; font-weight: 500; }
  .photo { position: absolute; }
  .photo-curves { background: linear-gradient(160deg, #f3f6fa 0%, #c9d3e0 45%, #5a6c86 70%, #e6ebf2 100%); }
  .photo-leaf { background: radial-gradient(circle at 40% 45%, #b9e27a 0%, #6fb63a 40%, #2f7a1c 100%); }
  .section-title { position: absolute; font-size: 10px; color: var(--navy); }
  .section-title.underlined { border-bottom: 1px solid var(--green); padding-bottom: 2px; }
  .section-title.strong { font-weight: 700; }
  .quote-mark { position: absolute; font-family: "Montserrat", Arial, sans-serif; font-weight: 700; font-size: 16px; color: var(--green); line-height: 1; }
  .body-copy { position: absolute; font-size: 4.8px; line-height: 1.45; color: #555; }
  .kicker { position: absolute; font-size: 4.8px; letter-spacing: .4px; color: var(--muted); }
  .inner .page-foot { bottom: 8px; }
</style>
</head>
<body>
<main class="sheet-grid">

  <!-- Report cover -->
  <section class="page cover">
    <div class="brand-block">
      <div class="brand-row"><span class="brand-dot"></span><span class="brand">Verdant Ridge Group</span></div>
      <div class="tagline">Clear Energy Thinking</div>
    </div>
    <h1 class="doc-title">[Document title]</h1>
    <div class="title-rule"></div>
    <p class="doc-sub">[DOCUMENT SUBTITLE]</p>
    <p class="doc-company">VERDANT RIDGE GROUP</p>
    <div class="edge-bar"></div>
    <footer class="page-foot">
      <div class="foot-rule"><span class="navy"></span><span class="green"></span></div>
      <div class="foot-text"><span class="site">verdantridgegroup.com</span><span class="mail">info@verdantridgegroup.com</span></div>
    </footer>
  </section>

  <!-- Letterhead -->
  <section class="page letter">
    <svg class="top-band" viewBox="0 0 290 30" aria-hidden="true">
      <line x1="0" y1="24" x2="150" y2="24" stroke="var(--navy)" stroke-width="1.5"/>
      <polygon points="150,22 170,12 290,12 290,16 175,16 155,26 150,26" fill="var(--navy)"/>
      <rect x="200" y="4" width="90" height="6" fill="var(--navy)"/>
    </svg>
    <div class="brand-block">
      <div class="brand-row"><span class="brand-dot"></span><span class="brand">Verdant Ridge Group</span></div>
      <div class="tagline">Clear Energy Thinking</div>
    </div>
    <div class="outline">
      <ol>
        <li>Single Template
          <ol class="lvl-b">
            <li>This template will be used for most day-to-day activities. The basic text page will often be used as a stand-alone one or several page document.</li>
            <li>The template should have the following characteristics:
              <ol class="lvl-i">
                <li>Styles should be defined and used for all common elements (e.g. Title, Subtitle, Header 1, Header 2, Header 3, body text and/or Normal, Bullets, numbers)</li>
                <li>We would like the headings in two different variants of Outline Form
                  <div class="bold">a) Sequential numbers:</div>
                  <ul><li>"1" Heading 1</li><li>"1.1" Heading 2</li><li>"1.1.1" Heading 3</li></ul>
                  <div class="bold">b) Other</div>
                  <ul><li>"I." Heading 1</li><li>"A." Heading 2</li><li>"1." Heading 3</li></ul>
                </li>
                <li>Left Justified without indent; bold and/or italics by level</li>
                <li>11 or 12 point font, sans serif fonts for headings, serif for text</li>
                <li>Simple column, header and footer</li>
                <li>Incorporate logo variants and colors</li>
              </ol>
            </li>
          </ol>
        </li>
      </ol>
    </div>
    <svg class="corner" viewBox="0 0 30 30" aria-hidden="true"><polygon points="30,0 30,30 0,30" fill="var(--lime)"/></svg>
    <footer class="page-foot">
      <div class="foot-rule"><span class="green"></span><span class="lime"></span></div>
      <div class="foot-text"><span class="site">verdantridgegroup.com</span><span class="mail">info@verdantridgegroup.com</span></div>
    </footer>
  </section>

  <!-- Project cover -->
  <section class="page project">
    <div class="bar-top"></div>
    <div class="bar-bottom"></div>
    <div class="brand-block">
      <div class="brand">Verdant Ridge Group</div>
      <div class="tag-line">Clear Energy Thinking</div>
    </div>
    <p class="pull-quote">[Grab your reader's attention with a great quote from the document or use this space to emphasize a key point. To place this text box anywhere on the page, just drag it.]</p>
    <footer class="page-foot">
      <div class="foot-rule"><span class="navy"></span><span class="lime"></span><span class="navy"></span><span class="green"></span></div>
      <div class="foot-text"><span class="site">verdantridgegroup.com</span><span class="mail">info@verdantridgegroup.com</span></div>
    </footer>
  </section>

  <!-- Interior: Advisor & Investor -->
  <section class="page inner">
    <header class="head"><div class="brand-row"><span class="brand-dot"></span><span class="brand">Verdant Ridge Group</span></div></header>
    <div class="photo photo-curves" role="img" aria-label="Photograph of sweeping white architectural curves" style="left:0;right:0;top:40px;height:100px;"></div>
    <h2 class="section-title underlined" style="left:16px;top:152px;width:130px;">Advisor &amp; Investor</h2>
    <span class="quote-mark" style="left:18px;top:172px;">“</span>
    <p class="body-copy" style="left:30px;top:188px;width:200px;font-weight:600;color:#333;">Success usually comes to those who are too busy to be looking for it.</p>
    <span class="quote-mark" style="left:230px;top:192px;">”</span>
    <p class="body-copy" style="left:16px;top:215px;width:258px;">We guide clients through every stage of the clean energy transition, from early feasibility studies to long term investment planning. Our advisors pair sound financial analysis with practical field experience, helping partners build portfolios that grow steadily, cut emissions and stay resilient as markets and policy change.</p>
    <footer class="page-foot">
      <div class="foot-rule"><span class="navy"></span><span class="green"></span></div>
      <div class="foot-text"><span class="site">verdantridgegroup.com</span><span class="mail">info@verdantridgegroup.com</span></div>
    </footer>
  </section>

  <!-- Interior: Acceptance of Proposal -->
  <section class="page inner">
    <header class="head"><div class="brand-row"><span class="brand-dot"></span><span class="brand">Verdant Ridge Group</span></div></header>
    <h2 class="section-title strong underlined" style="left:16px;top:45px;width:200px;">Acceptance of Proposal</h2>
    <p class="kicker" style="left:16px;top:70px;">LET'S GET TO WORK TOGETHER</p>
    <p class="body-copy" style="left:16px;top:82px;width:258px;">Once both parties accept this proposal, our team will schedule a kickoff meeting, confirm the project timeline and assign a dedicated lead. We believe open communication and shared goals are the foundation of every lasting partnership, and we look forward to delivering measurable results for your organisation.</p>
    <div class="photo photo-leaf" role="img" aria-label="Close-up photograph of water droplets on a green leaf" style="left:0;right:0;top:210px;height:170px;"></div>
    <footer class="page-foot">
      <div class="foot-rule"><span class="navy"></span><span class="green"></span></div>
      <div class="foot-text"><span class="site">verdantridgegroup.com</span><span class="mail">info@verdantridgegroup.com</span></div>
    </footer>
  </section>

  <!-- Interior: Heading -->
  <section class="page inner">
    <header class="head"><div class="brand-row"><span class="brand-dot"></span><span class="brand">Verdant Ridge Group</span></div></header>
    <div class="photo photo-leaf" role="img" aria-label="Photograph of dew drops on a bright green leaf" style="left:0;top:40px;width:120px;height:110px;"></div>
    <h2 class="section-title" style="left:130px;top:42px;">Heading</h2>
    <p class="body-copy" style="left:130px;top:58px;width:145px;">Our renewable energy specialists review each site, model expected output and outline the incentives available, so clients can compare options with confidence before committing any capital to new projects.</p>
    <h2 class="section-title" style="left:16px;top:165px;">Acceptance of Proposal</h2>
    <p class="body-copy" style="left:16px;top:182px;width:258px;">By signing below, the client confirms the scope, fees and schedule described in this document. Changes requested after approval will be reviewed jointly and documented in writing.</p>
    <div class="photo photo-leaf" role="img" aria-label="Photograph of water droplets on a green leaf" style="right:0;top:235px;width:120px;height:110px;"></div>
    <footer class="page-foot">
      <div class="foot-rule"><span class="navy"></span><span class="green"></span></div>
      <div class="foot-text"><span class="site">verdantridgegroup.com</span><span class="mail">info@verdantridgegroup.com</span></div>
    </footer>
  </section>

</main>
</body>
</html>
```